I am hosting a banquet called, Copper & Ivy Gala and I need a design to help sell it on Facebook.

Hi all.
No disco balls, please.
I would like a miser-traditional design, classy.

```html
<!DOCTYPE html>
<html lang="en">
<head>
<meta charset="utf-8">
<title>Copper &amp; Ivy Gala</title>
<link rel="stylesheet" href="https://fonts.googleapis.com/css2?family=Roboto:wght@700;900&family=Montserrat:wght@400;500;700&family=Yellowtail&family=Dancing+Script:wght@700&display=swap">
<style>
  :root {
    --night-top: #0f1618;
    --night-mid: #131c1e;
    --night-bottom: #263a3c;
    --mist-top: #e4f0f5;
    --mist-bottom: #a8c6ce;
    --ink: #2a2d35;
    --paper: #ffffff;
  }
  * { margin: 0; padding: 0; box-sizing: border-box; }
  html, body { width: 1200px; height: 1200px; overflow: hidden; background: #dedede; }
  .flyer { position: relative; width: 1200px; height: 1200px; overflow: hidden; }
  .panel-dark {
    position: absolute; left: 0; top: 0; width: 600px; height: 1200px;
    background: radial-gradient(ellipse at 75% 20%, #3a4a4c 0%, transparent 45%),
                linear-gradient(180deg, var(--night-top) 0%, var(--night-mid) 45%, var(--night-bottom) 100%);
  }
  .panel-light {
    position: absolute; left: 600px; top: 0; width: 600px; height: 1200px;
    background: radial-gradient(circle at 40% 55%, #f3f9fb 0%, transparent 55%),
                linear-gradient(180deg, var(--mist-top) 0%, #d3e5ec 60%, var(--mist-bottom) 100%);
  }
  .brand {
    position: absolute; left: 880px; top: 76px; width: 320px;
    font: 400 52px/1.22 "Montserrat", sans-serif; color: var(--ink); text-align: center;
  }
  .title-word {
    position: absolute; top: 458px;
    font: 900 142px/1 "Roboto", sans-serif; letter-spacing: -4px;
  }
  .title-left { right: 702px; color: var(--paper); }
  .title-right { left: 708px; color: var(--ink); }
  .amp-disc {
    position: absolute; left: 512px; top: 483px; width: 176px; height: 176px; border-radius: 50%;
    background: linear-gradient(90deg, var(--paper) 50%, var(--ink) 50%);
  }
  .amp-mark {
    position: absolute; left: 512px; top: 471px; width: 176px; text-align: center;
    font: 900 142px/1 "Roboto", sans-serif;
    background: linear-gradient(90deg, var(--ink) 50%, var(--mist-top) 50%);
    -webkit-background-clip: text; background-clip: text; color: transparent;
  }
  .script-word {
    position: absolute; right: 62px; top: 650px;
    font: 400 240px/1 "Yellowtail", "Dancing Script", cursive; color: var(--ink);
  }
  .blurb {
    position: absolute; left: 62px; top: 696px; width: 478px;
    font: 500 23px/32px "Montserrat", sans-serif; color: var(--paper);
    text-align: justify; hyphens: auto;
  }
  .info-band { position: absolute; top: 934px; height: 99px; display: flex; align-items: center; justify-content: center; font: 700 68px/1 "Roboto", sans-serif; letter-spacing: -1px; }
  .band-date { left: 62px; width: 538px; background: var(--paper); color: var(--ink); }
  .band-time { left: 600px; width: 538px; background: var(--ink); color: var(--paper); }
  .contact-phone {
    position: absolute; left: 100px; top: 1066px; display: flex; align-items: center; gap: 20px;
    font: 400 54px/1 "Montserrat", sans-serif; color: var(--paper);
  }
  .contact-place {
    position: absolute; left: 688px; top: 1062px; display: flex; align-items: center; gap: 20px;
    font: 700 25px/32px "Montserrat", sans-serif; color: var(--ink); letter-spacing: 0.5px;
  }
</style>
</head>
<body>
<main class="flyer">
  <div class="panel-dark" role="img" aria-label="Soft dark backdrop with blurred evening light"></div>
  <div class="panel-light" role="img" aria-label="Soft pale backdrop with diffused light"></div>

  <div class="brand">Ivy Hall<br>Events</div>

  <div class="title-word title-left">Copper</div>
  <div class="amp-disc"></div>
  <div class="amp-mark">&amp;</div>
  <div class="title-word title-right">Ivy</div>
  <div class="script-word">Gala</div>

  <p class="blurb">Lorem ipsum dolor sit amet, consectetur adipiscing elit, sed do eiusmod tempor incididunt ut labore et dolore magna aliqua. Ut enim ad minim veniam, quis nostrud exercitation ullamco laboris nisi ut aliquip</p>

  <div class="info-band band-date">April 16, 2023</div>
  <div class="info-band band-time">At 6:30 pm</div>

  <div class="contact-phone">
    <svg width="50" height="50" viewBox="0 0 24 24" fill="#fff" aria-hidden="true">
      <path d="M6.6 10.8a15.1 15.1 0 0 0 6.6 6.6l2.2-2.2a1 1 0 0 1 1-.25 11.4 11.4 0 0 0 3.6.57 1 1 0 0 1 1 1V20a1 1 0 0 1-1 1A17 17 0 0 1 3 4a1 1 0 0 1 1-1h3.5a1 1 0 0 1 1 1c0 1.250.2 2.450.57 3.570a1 1 0 0 1-.25 1z"/>
      <path d="M14 2.5a7.5 7.5 0 0 1 7.5 7.5h-1.6A5.9 5.9 0 0 0 14 4.1zM14 6a4 4 0 0 1 4 4h-1.6A2.4 2.4 0 0 0 14 7.6z"/>
    </svg>
    <span>+1 555 014 7788</span>
  </div>

  <div class="contact-place">
    <svg width="36" height="52" viewBox="0 0 24 34" fill="#2a2d35" aria-hidden="true">
      <path d="M12 0A12 12 0 0 0 0 12c0 9 12 22 12 22s12-13 12-22A12 12 0 0 0 12 0zm0 17a5 5 0 1 1 0-10 5 5 0 0 1 0 10z"/>
    </svg>
    <span>742 Linden Avenue, Hart<br>well 20417, United States</span>
  </div>
</main>
</body>
</html>
```